Redesign business card for Wade Linford Construction

Basically I want a complete redesign of the business card I have attached with this project. The only stipulations I have are that the colors , crimson and white, stay the same and all of the information on the old card is also on the new design. Also I would like to add that we also specialize in metal building foundations as well. I look forward to seeing what you all come up with.
Industry/Entity Type
Business
Contact Information for Business Card
All of the details are on the attachment I have included with this project
Look and feel
Each slider illustrates characteristics of the customer's brand and the style your logo design should communicate.

```html
<!DOCTYPE html>
<html lang="en">
<head>
<meta charset="utf-8">
<title>Wade Linford Construction – Business Card</title>
<link href="https://fonts.googleapis.com/css2?family=Archivo:wght@400;600;800&display=swap" rel="stylesheet">
<style>
  :root {
    --crimson: #e8232b;
    --white: #ffffff;
    --card-white: #f7f7f5;
    --panel-grey: #ececea;
    --ink-grey: #4a4a4a;
    --stage: #e4e1dc;
  }
  * { box-sizing: border-box; margin: 0; padding: 0; }
  html, body { width: 1200px; height: 1000px; overflow: hidden; }
  body {
    background: var(--stage);
    font-family: "Archivo", Arial, sans-serif;
    position: relative;
  }
  .card {
    position: absolute;
    width: 630px;
    height: 360px;
    border-radius: 4px;
    box-shadow: 0 10px 30px rgba(0,0,0,0.18);
    overflow: hidden;
  }

  /* Front */
  .card-front {
    left: 80px; top: 100px;
    background: var(--crimson);
    color: var(--white);
    display: flex;
    flex-direction: column;
    align-items: center;
    justify-content: center;
    text-align: center;
  }
  .front-square {
    width: 64px; height: 64px;
    border: 6px solid var(--white);
    margin-bottom: 26px;
  }
  .front-name {
    font-weight: 800;
    font-size: 30px;
    line-height: 1.1;
    letter-spacing: 2px;
    text-transform: uppercase;
  }
  .front-tagline {
    margin-top: 8px;
    font-weight: 400;
    font-size: 16px;
    letter-spacing: 3px;
    text-transform: uppercase;
  }

  /* Back */
  .card-back {
    left: 490px; top: 540px;
    background: var(--card-white);
    color: var(--ink-grey);
  }
  .back-panel {
    position: absolute;
    right: 0; top: 70px;
    width: 250px; height: 180px;
    background: var(--panel-grey);
  }
  .back-brand {
    position: absolute;
    left: 34px; top: 30px;
    display: flex;
    align-items: center;
    gap: 12px;
  }
  .back-square {
    width: 30px; height: 30px;
    border: 4px solid var(--crimson);
  }
  .back-name {
    color: var(--crimson);
    font-weight: 800;
    font-size: 19px;
    letter-spacing: 1px;
    text-transform: uppercase;
    line-height: 1.1;
  }
  .back-tagline {
    position: absolute;
    left: 76px; top: 58px;
    font-size: 11px;
    letter-spacing: 2px;
    text-transform: uppercase;
    color: var(--ink-grey);
  }
  .person {
    position: absolute;
    left: 34px; top: 104px;
  }
  .person-name {
    color: var(--crimson);
    font-weight: 800;
    font-size: 20px;
  }
  .person-role {
    font-size: 13px;
    letter-spacing: 1px;
    text-transform: uppercase;
    margin-top: 2px;
  }
  .contact-list {
    list-style: none;
    position: absolute;
    left: 34px; top: 160px;
    font-size: 14px;
    line-height: 1.5;
  }
  .contact-list li { display: flex; align-items: flex-start; gap: 8px; }
  .contact-icon { width: 12px; height: 12px; margin-top: 4px; flex: none; fill: var(--crimson); }
  .specialties {
    position: absolute;
    right: 30px; top: 264px;
    width: 290px;
    font-weight: 600;
    font-size: 12px;
    line-height: 1.35;
    color: var(--ink-grey);
  }
</style>
</head>
<body>

<section class="card card-front" aria-label="Card front">
  <div class="front-square"></div>
  <div class="front-name">Wade Linford<br>Construction</div>
  <div class="front-tagline">Concrete Contractor</div>
</section>

<section class="card card-back" aria-label="Card back">
  <div class="back-panel"></div>

  <div class="back-brand">
    <div class="back-square"></div>
    <div class="back-name">Wade Linford Construction</div>
  </div>
  <div class="back-tagline">Concrete Contractor</div>

  <div class="person">
    <div class="person-name">Wade Linford</div>
    <div class="person-role">Owner</div>
  </div>

  <ul class="contact-list">
    <li>
      <svg class="contact-icon" viewBox="0 0 12 12"><path d="M2 0h3l1 3-2 1.2a7 7 0 0 0 3.8 3.8L9 6l3 1v3a2 2 0 0 1-2 2A10 10 0 0 1 0 2a2 2 0 0 1 2-2z"/></svg>
      <span>555.214.3370</span>
    </li>
    <li>
      <svg class="contact-icon" viewBox="0 0 12 12"><path d="M3 0h6a1 1 0 0 1 1 1v10a1 1 0 0 1-1 1H3a1 1 0 0 1-1-1V1a1 1 0 0 1 1-1zm0 2v7h6V2zm3 8a.7.7 0 1 0 0 .01z"/></svg>
      <span>555.214.3371</span>
    </li>
    <li>
      <svg class="contact-icon" viewBox="0 0 12 12"><path d="M3 0h6v3H3zM1 4h10a1 1 0 0 1 1 1v5H0V5a1 1 0 0 1 1-1zm2 4v4h6V8z"/></svg>
      <span>555.608.1924</span>
    </li>
    <li>
      <svg class="contact-icon" viewBox="0 0 12 12"><path d="M0 2h12v8H0zm1 1v.4l5 3.3 5-3.3V3z"/></svg>
      <span>wlconcrete@mailbox.com</span>
    </li>
    <li>
      <svg class="contact-icon" viewBox="0 0 12 12"><path d="M6 0a4 4 0 0 1 4 4c0 3-4 8-4 8S2 7 2 4a4 4 0 0 1 4-4zm0 2.4a1.6 1.6 0 1 0 0 3.2 1.6 1.6 0 0 0 0-3.2z"/></svg>
      <span>218 Ridge Mill Rd.<br>Millbrook Falls, AL 36000</span>
    </li>
  </ul>

  <p class="specialties">Specializing in concrete foundations, metal building foundations, driveways, storm rooms, additions and most other forms of concrete work.</p>
</section>

</body>
</html>
```